New Menu Design Project

Would like a menu designed..

SIZE A4 - double sided..

One on side, we would like our regular menu, on the other side we would like our catering options.
I have attached both files/
I have also attached our logo

Target Market(s)

We are located at a hospital, so we target hospital staff and also university students.

Industry/Entity Type

Catering

```html
<!DOCTYPE html>
<html lang="en">
<head>
<meta charset="utf-8">
<title>Catering Menu</title>
<link href="https://fonts.googleapis.com/css2?family=Raleway:ital,wght@0,400;0,500;0,600;0,700;0,800;1,400;1,500&display=swap" rel="stylesheet">
<style>
:root{
  --ink:#4a4f56;
  --red:#d6203a;
  --paper:#ffffff;
  --sand:#ebe6da;
}
*{margin:0;padding:0;box-sizing:border-box}
html,body{width:848px;height:1200px;overflow:hidden;background:var(--paper)}
body{font-family:'Raleway',sans-serif;color:var(--ink);position:relative}
.page{position:relative;width:848px;height:1200px}
.title{position:absolute;left:40px;top:18px;font-size:70px;font-weight:800;letter-spacing:1px;line-height:1}
.contact{position:absolute;left:467px;top:24px;line-height:1.38}
.contact .hours{font-size:13px}
.contact .hours b{font-weight:700}
.contact .visit{font-style:italic;font-size:15px;text-transform:uppercase}
.contact .call{font-size:15.5px;text-transform:uppercase}
.contact .call b{font-weight:800}
.frame{position:absolute;left:52px;top:106px;width:778px;height:1076px;border:3px solid var(--red)}
.divider{position:absolute;left:350px;top:128px;width:1px;height:594px;background:#cfcfcf}
.heading{font-weight:700;font-size:22px;letter-spacing:2px;text-align:center;text-transform:uppercase;line-height:28px}
.heading::before,.heading::after{content:"•";color:var(--red);margin:0 8px}
.col-left{position:absolute;left:70px;top:120px;width:272px}
.row{display:flex;font-size:8.6px;line-height:15.4px;font-weight:500;text-transform:uppercase}
.row .name{width:203px}
.row .price{flex:1;text-transform:none}
.row.sub{font-style:italic;text-transform:none;padding-left:22px;line-height:12px}
.row.meat{text-transform:none}
.lunch .row{line-height:16.2px}
.lunch .row.sub{line-height:11.6px}
.light{margin-top:8px}
.crosses{display:flex;gap:14px;justify-content:center;margin:14px 0 6px}
.lunch-note{font-style:italic;font-size:12px;text-align:center;line-height:14px;margin:12px 0 18px;text-transform:uppercase}
.col-right{position:absolute;left:370px;top:120px;width:440px}
.group{display:flex;align-items:baseline;gap:14px;margin-top:10px;margin-bottom:1px}
.group .label{color:var(--red);font-weight:700;font-size:14px;text-transform:uppercase}
.group .label small{color:var(--ink);font-size:9px;font-style:italic;font-weight:500;text-transform:none}
.group .each{font-size:13px;font-weight:500}
.item{font-size:8.3px;line-height:16.6px;white-space:nowrap}
.item b{font-weight:700;text-transform:uppercase}
.item i{font-weight:400}
.brand{position:absolute;left:370px;top:732px;width:120px;height:120px;border-radius:50%;background:var(--red);display:flex;align-items:center;justify-content:center;color:#fff;font-weight:800;font-size:18px;letter-spacing:.5px}
.decor{position:absolute;border-radius:60px 60px 30px 30px;background:linear-gradient(180deg,var(--sand),#f3efe6);opacity:.8}
.decor.left{left:90px;top:742px;width:220px;height:310px}
.decor.right{left:580px;top:742px;width:220px;height:310px}
.hot{position:absolute;left:52px;top:878px;width:778px;text-align:center}
.hot .sub{font-size:11px;font-weight:700;margin-top:2px}
.hot-cols{position:absolute;left:52px;top:928px;width:778px;display:grid;grid-template-columns:236px 300px 242px;text-align:center}
.hot-cols h3{color:var(--red);font-size:11px;font-weight:700;text-transform:uppercase;margin-bottom:4px}
.dish{font-size:9px;font-weight:600;text-transform:uppercase;line-height:12px}
.desc{font-size:8.4px;font-style:italic;line-height:10.6px;margin-bottom:4px}
.meat-list .dish{line-height:13px}
.footer-email{position:absolute;left:74px;top:1094px;font-size:10px;font-weight:600}
.footer-social{position:absolute;left:598px;top:1088px;display:flex;align-items:center;gap:8px;font-size:12px;font-weight:500}
.footer-social .sq{width:20px;height:20px;background:var(--ink);border-radius:3px}
</style>
</head>
<body>
<div class="page">
  <h1 class="title">CATERING</h1>
  <div class="contact">
    <p class="hours">Trading hours: <b>Monday to Friday 6am to 4pm</b></p>
    <p class="visit">Visit us in store to discuss catering options</p>
    <p class="call">or call <b>Mara</b> on <b>0412 555 019</b></p>
  </div>

  <div class="frame"></div>
  <div class="divider"></div>

  <div class="decor left" role="img" aria-label="Decorative cutlery illustration in soft beige"></div>
  <div class="decor right" role="img" aria-label="Decorative cutlery illustration in soft beige"></div>

  <section class="col-left">
    <h2 class="heading">Light Options</h2>
    <div class="light">
      <div class="row"><span class="name">Bacon and egg muffins</span><span class="price">$4.50</span></div>
      <div class="row"><span class="name">Savory muffin</span><span class="price">$5.50</span></div>
      <div class="row sub">garden vegetable or</div>
      <div class="row sub">pumpkin and bacan</div>
      <div class="row"><span class="name">Muffin of the day</span><span class="price">$4.50</span></div>
      <div class="row"><span class="name">Brekky bar</span><span class="price">$4.00</span></div>
      <div class="row"><span class="name">Assorted yoghurts</span><span class="price">$4.50 each</span></div>
      <div class="row"><span class="name">Bircher muesli</span><span class="price">$4.50 each</span></div>
      <div class="row"><span class="name">Chia pudding</span><span class="price">$4.50 each</span></div>
      <div class="row"><span class="name">Banana bread</span><span class="price">$4.50 each</span></div>
      <div class="row sub">or BANANA AND WALNUT BREAD</div>
      <div class="row"><span class="name">Assorted slices</span><span class="price">$4.00 each</span></div>
      <div class="row sub">lemon/caramel/hedgehog/rocky road</div>
    </div>
    <div class="crosses">
      <svg width="22" height="22" viewBox="0 0 22 22"><path d="M8 0h6v8h8v6h-8v8H8v-8H0V8h8z" fill="var(--red)"/></svg>
      <svg width="22" height="22" viewBox="0 0 22 22"><path d="M8 0h6v8h8v6h-8v8H8v-8H0V8h8z" fill="var(--red)"/></svg>
      <svg width="22" height="22" viewBox="0 0 22 22"><path d="M8 0h6v8h8v6h-8v8H8v-8H0V8h8z" fill="var(--red)"/></svg>
    </div>
    <h2 class="heading">Lunch</h2>
    <p class="lunch-note">Lunch options change daily;<br>please call to discuss<br>what is available</p>
    <div class="lunch">
      <div class="row"><span class="name">Beef sliders</span><span class="price">$5.00 each</span></div>
      <div class="row"><span class="name">Pasta of the day</span><span class="price">$9.50 per serve</span></div>
      <div class="row"><span class="name">Spanakopita</span><span class="price">$7.50 per serve</span></div>
      <div class="row"><span class="name">Pumpkin, spinach &amp; feta filo</span><span class="price">$7.50</span></div>
      <div class="row sub">(can be cut into 3)</div>
      <div class="row"><span class="name">Chicken &amp; asparagus filo</span><span class="price">$7.50</span></div>
      <div class="row sub">(can be cut into 3)</div>
      <div class="row"><span class="name">Satay chicken filo</span><span class="price">$7.50</span></div>
      <div class="row sub">(can be cut into 3)</div>
      <div class="row"><span class="name">Salmon patties</span><span class="price">$7.50</span></div>
      <div class="row"><span class="name">Frittata</span><span class="price">$7.50</span></div>
      <div class="row"><span class="name">Thai chicken tortilla bake</span><span class="price">$7.50</span></div>
      <div class="row"><span class="name">Vegetarian salads</span><span class="price">$7.50 per serve</span></div>
      <div class="row meat"><span class="name">Meat/seafood salads</span><span class="price">$9.50 per serve</span></div>
    </div>
  </section>

  <section class="col-right">
    <h2 class="heading">Sandwich Options</h2>
    <div class="group"><span class="label">Focaccias <small>(Toasted and cut into 2)</small></span><span class="each">$7.50 each</span></div>
    <p class="item"><b>Chicken schnitzel</b> <i>butter, mayo, lettuce, cheese, tomato and schnitzel</i></p>
    <p class="item"><b>Ham</b> <i>butter, pickle spread, cheese, tomato and ham</i></p>
    <p class="item"><b>Salami</b> <i>butter, pesto, spinach, salami roast capsicum, feta, olives and salami</i></p>
    <p class="item"><b>Sweet chili chicken</b> <i>butter, sweet chili sauce, spinach, chicken tenders, cheese, tomato</i></p>
    <p class="item"><b>Chicken and avocado</b> <i>butter, mayo, lettuce, tomato, cheese, chicken and avocado</i></p>
    <p class="item"><b>Roast vegetables</b> <i>butter, pesto, spinach, roast eggplant, zucchini, capsicum and feta</i></p>
    <p class="item"><b>Roast beef</b> <i>butter, Dijon, spinach, beef, cheese, tomato</i></p>

    <div class="group"><span class="label">Sandwiches</span><span class="each">$6.00 each</span></div>
    <p class="item"><b>Chicken schnitzel</b> <i>butter, mayo, lettuce, cheese, tomato and schnitzel</i></p>
    <p class="item"><b>Turkey</b> <i>butter, cranberry sauce, spinach, tomato, cucumber, cheese and turkey</i></p>
    <p class="item"><b>Ham</b> <i>butter, pickle spread, cheese, tomato and ham</i></p>
    <p class="item"><b>Tandoori chicken</b> <i>butter, tziki, spinach, tomato, cucumber and chicken</i></p>
    <p class="item"><b>Chicken and avocado</b> <i>butter, mayo, lettuce, tomato, cheese, chicken and avocad</i></p>
    <p class="item"><b>Egg mix</b> <i>butter, mayo, lettuce and egg</i></p>
    <p class="item"><b>Tuna mix</b> <i>butter, mayo, lettuce and tuna mix</i></p>
    <p class="item"><b>Roast vegetables</b> <i>butter, pesto, spinach, roast eggplant, zucchini, capsicum and feta</i></p>
    <p class="item"><b>Chicken and capsicum</b> <i>butter, mayo, chicken &amp; capsicum mix &amp; lettuce</i></p>
    <p class="item"><b>Salami and pesto</b> <i>butter, pesto, salami &amp; tasty cheese</i></p>
    <p class="item"><b>Roast beef</b> <i>butter, Dijon, spinach, beef, cheese, tomato</i></p>
    <p class="item"><b>BLT</b> <i>butter, bacon, lettuce, tomato</i></p>

    <div class="group"><span class="label">Wraps <small>(cut into 3)</small></span><span class="each">$7.50 each</span></div>
    <p class="item"><b>Chicken schnitzel</b> <i>butter, mayo, lettuce, cheese, tomato and schnitzel</i></p>
    <p class="item"><b>Turkey</b> <i>butter, cranberry sauce, spinach, tomato, cucumber, cheese and turkey</i></p>
    <p class="item"><b>Ham</b> <i>butter, pickle spread, cheese, tomato and ham</i></p>
    <p class="item"><b>Tandoori chicken</b> <i>butter, tziki, spinach, tomato, cucumber and chicken</i></p>
    <p class="item"><b>Chicken and avocado</b> <i>butter, mayo, lettuce, tomato, cheese, chicken and avocado</i></p>
    <p class="item"><b>BLT</b> <i>butter, bacon, lettuce, tomato</i></p>
    <p class="item"><b>Sweet chili chicken</b> <i>butter, sweet chili sauce, spinach, chicken tenders, cheese, tomato</i></p>
    <p class="item"><b>Egg mix</b> <i>butter, mayo, lettuce and egg</i></p>
    <p class="item"><b>Tuna mix</b> <i>butter, mayo, lettuce and tuna mix</i></p>
  </section>

  <div class="brand">Wardside</div>

  <div class="hot">
    <h2 class="heading">Hot Food Catering</h2>
    <p class="sub">($2.00 per item)</p>
  </div>

  <div class="hot-cols">
    <div class="seafood">
      <h3>Seafood Options</h3>
      <p class="dish">Potato spun prawns</p>
      <p class="desc">tiger prawns wrapped in a<br>crunchy potato noodle</p>
      <p class="dish">Crumbed whiting fillets</p>
      <p class="desc">mini whiting filets encrusted in a crisp,<br>light style crumb</p>
      <p class="dish">Calamari rings</p>
      <p class="desc">squid rings in a golden crispy crumb</p>
    </div>
    <div class="vegetarian">
      <h3>Vegetarian Options</h3>
      <p class="dish">Three cheese and vegetable filo triangles</p>
      <p class="desc">a tasty blend of feta, ricotta and pecorino cheeses<br>with a selection of vegetables encased in a crispy filo pastry</p>
      <p class="dish">Mini spinach and ricotta rolls</p>
      <p class="desc">delicious pastry parcels filled with baby spinach and creamy ricotta</p>
      <p class="dish">Cheese and broccoli bites</p>
      <p class="desc">delicious bite sized goodness filled with cheese and broccoli</p>
      <p class="dish">Mini samosa</p>
      <p class="desc">add an exotic taste to your next catering menu</p>
      <p class="dish">Cocktail vegetarian spring rolls</p>
      <p class="desc">bite sized pieces ideal for corporate meetings and snacks</p>
      <p class="dish">Mini frittata</p>
      <p class="desc">a colourful roast veggie medley backed in a light frittata</p>
    </div>
    <div class="meat-list">
      <h3>Meat &amp; Poultry Options</h3>
      <p class="dish">Mini chicken garlic kiev</p>
      <p class="desc">bite sized chicken pieces with a garlic center</p>
      <p class="dish">Satay chicken skewers</p>
      <p class="dish">Party pies &amp; sausage rolls</p>
      <p class="dish">Assorted mini quiche</p>
      <p class="dish">Mini beef dim sims</p>
      <p class="dish">Sweet chili chicken tenders</p>
      <p class="dish">Mini beef meatballs</p>
    </div>
  </div>

  <p class="footer-email">email: mara@wardsidecanteen.com</p>
  <div class="footer-social"><span class="sq"></span><span>@wardsidecanteen</span></div>
</div>
</body>
</html>
```